Livestock Consulting Company has a logo but needs business cards and a uniform logo

My company works with farmers advising them on managing cattle and sheep. I have a logo but need business cards and a version of my logo to go onto my work shirts. I need the following wording added to my logo for my shirts "Tallowby Livestock Consulting".

```html
<!DOCTYPE html>
<html lang="en">
<head>
<meta charset="utf-8">
<title>Tallowby Livestock Consulting – Business Cards</title>
<link href="https://fonts.googleapis.com/css2?family=Cinzel:wght@400;500&family=Arimo:wght@400&display=swap" rel="stylesheet">
<style>
  :root {
    --backdrop: #1e1e1e;
    --card: #0d0d0d;
    --card-edge: #161616;
    --gold: #a8875a;
    --ink-light: #ececec;
    --rule: #3a3a3a;
  }
  html, body {
    margin: 0;
    padding: 0;
    width: 1200px;
    height: 900px;
    overflow: hidden;
    background: var(--backdrop);
  }
  .canvas {
    position: relative;
    width: 1200px;
    height: 900px;
  }
  .card {
    position: absolute;
    left: 250px;
    width: 700px;
    height: 400px;
    background: radial-gradient(circle at 60% 35%, var(--card-edge), var(--card) 70%);
    box-shadow: 0 10px 30px rgba(0,0,0,0.55);
    box-sizing: border-box;
  }
  .card--front { top: 35px; }
  .card--back { top: 465px; }

  .brand {
    display: flex;
    align-items: center;
    gap: 14px;
  }
  .brand__dot {
    width: 18px;
    height: 18px;
    border-radius: 50%;
    background: var(--gold);
    flex: none;
  }
  .brand__name {
    font-family: "Cinzel", serif;
    font-weight: 500;
    color: var(--gold);
    letter-spacing: 0.06em;
    line-height: 1.15;
    margin: 0;
  }

  /* Front card */
  .front__brand {
    position: absolute;
    left: 40px;
    top: 0;
    width: 250px;
    height: 100%;
    display: flex;
    align-items: center;
  }
  .front__brand .brand__name { font-size: 24px; }
  .front__divider {
    position: absolute;
    left: 318px;
    top: 70px;
    width: 1px;
    height: 260px;
    background: var(--rule);
  }
  .front__details {
    position: absolute;
    left: 350px;
    top: 72px;
    font-family: "Arimo", sans-serif;
    color: var(--ink-light);
  }
  .person__name {
    font-family: "Cinzel", serif;
    font-weight: 500;
    color: var(--gold);
    font-size: 30px;
    letter-spacing: 0.04em;
    margin: 0;
  }
  .person__title {
    font-size: 19px;
    margin: 2px 0 18px;
  }
  .contact-list {
    list-style: none;
    margin: 0;
    padding: 0;
    font-size: 19px;
  }
  .contact-list li {
    display: flex;
    align-items: center;
    gap: 10px;
    margin-bottom: 4px;
  }
  .contact-list svg {
    width: 17px;
    height: 17px;
    flex: none;
  }
  .contact-list .accent { color: var(--gold); }
  .address {
    font-size: 19px;
    margin: 18px 0 0 27px;
    line-height: 1.3;
  }

  /* Back card */
  .card--back .brand {
    position: absolute;
    inset: 0;
    justify-content: center;
  }
  .card--back .brand__name { font-size: 28px; }
</style>
</head>
<body>
<main class="canvas">

  <section class="card card--front" aria-label="Business card front">
    <div class="front__brand">
      <div class="brand">
        <span class="brand__dot"></span>
        <p class="brand__name">Tallowby<br>Livestock<br>Consulting</p>
      </div>
    </div>
    <div class="front__divider"></div>
    <div class="front__details">
      <h1 class="person__name">MARCUS ELDEN</h1>
      <p class="person__title">Managing Director</p>
      <ul class="contact-list">
        <li>
          <svg viewBox="0 0 24 24" aria-hidden="true"><path fill="none" stroke="var(--gold)" stroke-width="2.2" stroke-linecap="round" d="M6 3l3 4-2 2c1 3 4 6 7 7l2-2 4 3-2 3C10 20 4 14 3 5z"/></svg>
          044-555 010 212
        </li>
        <li>
          <svg viewBox="0 0 24 24" aria-hidden="true"><rect x="2.5" y="5" width="19" height="14" fill="none" stroke="var(--ink-light)" stroke-width="2"/><path d="M3 6l9 7 9-7" fill="none" stroke="var(--ink-light)" stroke-width="2"/></svg>
          info@tallowby.com
        </li>
        <li>
          <svg viewBox="0 0 24 24" aria-hidden="true"><circle cx="12" cy="12" r="9" fill="none" stroke="var(--gold)" stroke-width="2"/><path d="M3 12h18M12 3c-4 5-4 13 0 18M12 3c4 5 4 13 0 18" fill="none" stroke="var(--gold)" stroke-width="1.6"/></svg>
          <span>www.<span class="accent">tallowby</span>.com</span>
        </li>
      </ul>
      <p class="address">18, Mill Lane, Harrowfield<br>70318, Northshire</p>
    </div>
  </section>

  <section class="card card--back" aria-label="Business card back">
    <div class="brand">
      <span class="brand__dot"></span>
      <p class="brand__name">Tallowby Livestock Consulting</p>
    </div>
  </section>

</main>
</body>
</html>
```